Harold Brisk Mechanical business cards

We need business cards designed for "Harold Brisk Mechanical" "Mechanical & Electrical Contractors" "Specializing in Service & Installation"
"Cooling, Heating, Service, Installations, Residential, Commercial"

```html
<!DOCTYPE html>
<html lang="en">
<head>
<meta charset="utf-8">
<title>Harold Brisk Mechanical – Business Cards</title>
<link rel="stylesheet" href="https://fonts.googleapis.com/css2?family=Roboto:wght@400;500;700&display=swap">
<style>
  :root {
    --page: #e9e7e3;
    --card: #ffffff;
    --ink: #1d1d1f;
    --red: #ec1c2c;
    --red-light: #f0404d;
    --grey: #5b5b5e;
    --white: #ffffff;
  }
  * { box-sizing: border-box; margin: 0; padding: 0; }
  html, body {
    width: 1200px; height: 768px; overflow: hidden;
    background: var(--page);
    font-family: "Roboto", Arial, sans-serif;
    color: var(--ink);
  }
  .sheet {
    position: relative; width: 1200px; height: 768px;
    display: flex; align-items: center; justify-content: center; gap: 40px;
  }
  .card {
    position: relative; width: 540px; height: 309px;
    background: var(--card);
    box-shadow: 0 6px 18px rgba(0,0,0,.18);
    overflow: hidden;
  }

  /* Front */
  .front .company {
    position: absolute; left: 34px; bottom: 92px;
    display: flex; align-items: center; gap: 10px;
  }
  .mark-square { width: 14px; height: 14px; background: var(--red); flex: none; }
  .company-name {
    font-weight: 700; font-size: 21px; line-height: 1.1;
    text-transform: uppercase; letter-spacing: -.3px; color: var(--ink);
    width: 200px;
  }
  .contact-panel {
    position: absolute; top: 0; right: 0; width: 318px; height: 260px;
    background: linear-gradient(160deg, var(--red-light), var(--red));
    clip-path: polygon(24% 0, 100% 0, 100% 100%, 0 100%);
    color: var(--white);
    padding: 38px 26px 0 96px;
    text-align: right;
  }
  .person-name { font-weight: 700; font-size: 20px; letter-spacing: .3px; }
  .person-role { font-weight: 500; font-size: 12px; margin-top: 2px; margin-bottom: 22px; }
  .contact-line { font-size: 11px; line-height: 1.75; white-space: nowrap; }

  /* Back */
  .back { display: flex; flex-direction: column; align-items: center; justify-content: center; gap: 26px; }
  .back .services {
    font-size: 12px; color: var(--grey); letter-spacing: .3px;
  }
  .services .dot { color: var(--red); margin: 0 5px; }
  .logo-lockup { display: flex; align-items: center; gap: 14px; }
  .logo-lockup .mark-square { width: 30px; height: 30px; }
  .logo-lockup .company-name { font-size: 30px; width: auto; }
</style>
</head>
<body>
<main class="sheet">
  <section class="card front" aria-label="Business card front">
    <div class="company">
      <span class="mark-square"></span>
      <p class="company-name">Harold Brisk Mechanical</p>
    </div>
    <div class="contact-panel">
      <p class="person-name">DANIEL REYES</p>
      <p class="person-role">CEO/FOUNDER</p>
      <p class="contact-line">4120 Birchwood Drive Juneau, Alaska 99801</p>
      <p class="contact-line">P: 907 555 0142 &nbsp;M: 907 555 0187</p>
      <p class="contact-line">F: 907 555 0163 &nbsp;E: daniel@haroldbrisk.com</p>
      <p class="contact-line">W: www.haroldbrisk.com</p>
    </div>
  </section>

  <section class="card back" aria-label="Business card back">
    <p class="services">Cooling<span class="dot">•</span>Heating<span class="dot">•</span>Service<span class="dot">•</span>Installations</p>
    <div class="logo-lockup">
      <span class="mark-square"></span>
      <p class="company-name">Harold Brisk Mechanical</p>
    </div>
    <p class="services">Residential<span class="dot">•</span>Commercial</p>
  </section>
</main>
</body>
</html>
```